Graphic design on webpages considering optimisation

Hi,

I would like to make the pages of my website look better. The looks must tie with the landing page, which I will not change.

Ping me an email with any questions. I have been on Sketch Harbor for the brimvault.com page and am very pleased with its looks.

Industry/Entity Type

Graphic Design

```html
<!DOCTYPE html>
<html lang="fr">
<head>
<meta charset="utf-8">
<title>Brimvault – Le logiciel CRM Cloud</title>
<link rel="stylesheet" href="https://fonts.googleapis.com/css2?family=Open+Sans:wght@300;400;600;700&display=swap">
<style>
:root{
  --page-bg:#efefef;
  --white:#ffffff;
  --charcoal:#595959;
  --charcoal-dark:#333333;
  --blue:#1f7bb6;
  --blue-line:#2f8fc9;
  --text:#555555;
  --text-soft:#6a6a6a;
  --footer-text:#e6e6e6;
  --footer-muted:#bdbdbd;
  --border:#d9d9d9;
  --badge-navy:#26344f;
  --badge-ink:#111111;
  --badge-deep:#17325c;
  --badge-lilac:#f2f0f6;
  --badge-sand:#ece6dc;
}
*{margin:0;padding:0;box-sizing:border-box}
html,body{width:1079px;height:1200px;overflow:hidden}
body{background:var(--page-bg);font-family:"Open Sans",Arial,sans-serif;color:var(--text);position:relative}
.site{position:absolute;left:132px;top:15px;width:816px}
.lang-bar{height:19px;background:var(--charcoal);color:var(--white);font-size:9.5px;display:flex;justify-content:flex-end;align-items:center;padding-right:16px;gap:6px}
.lang-bar .sep{font-size:8px;opacity:.8}
.header{height:83px;background:var(--white);display:flex;align-items:center;justify-content:space-between;padding:0 26px 0 27px}
.brand{display:flex;align-items:center;gap:8px;font-weight:700;font-size:22px;letter-spacing:2px;color:#7a7a7a}
.brand-mark{width:14px;height:14px;background:var(--blue)}
.phone{display:flex;align-items:center;gap:11px;font-size:16px;font-weight:600;color:var(--text)}
.phone-icon{width:35px;height:35px;border-radius:50%;background:var(--blue);display:flex;align-items:center;justify-content:center}
.nav{display:flex;height:40px;background:var(--blue);list-style:none}
.nav li{display:flex;align-items:center;justify-content:center;color:var(--white);font-size:11.5px;font-weight:600;position:relative}
.nav li+li::before{content:"";position:absolute;left:0;top:9px;height:22px;width:1px;background:var(--blue-line)}
.nav li.active{background:var(--charcoal)}
.nav li.active+li::before{display:none}
.hero{height:152px;background:linear-gradient(90deg,#e3b59a 0%,#d9a98c 14%,#9aa3ad 30%,#c7cdd3 50%,#b4bcc5 68%,#3f5c86 84%,#6d7e94 100%)}
.content{height:441px;background:var(--white);position:relative;overflow:hidden}
.awards-card{position:absolute;left:26px;top:27px;width:221px;height:270px;border:1px solid var(--border);border-bottom:3px solid var(--blue);border-radius:4px;background:linear-gradient(#fafafa,#ffffff)}
.awards-card h2{font-weight:400;font-size:21px;line-height:25px;text-align:center;color:var(--text);margin-top:15px}
.awards-card .rule{width:32px;height:2px;background:var(--charcoal);margin:6px auto 0}
.badges{position:absolute;left:12px;top:100px}
.partner-card{position:absolute;left:26px;top:321px;width:223px;height:85px;border:1px solid var(--border);border-radius:4px;background:linear-gradient(#ffffff,#f3f3f3);display:flex;align-items:center;justify-content:center;gap:8px}
.partner-card .square{width:22px;height:22px;background:#1e4d7a}
.partner-card .name{font-size:15px;font-weight:600;color:#222;letter-spacing:.5px}
.article{position:absolute;left:282px;top:44px;width:510px}
.article h1{font-size:22px;font-weight:600;color:var(--text);margin-bottom:14px}
.article p,.article li{font-size:11.2px;line-height:19.2px;color:var(--text-soft)}
.article ul{list-style:none;margin-top:24px}
.article li{position:relative;padding-left:22px;margin-bottom:26px}
.article li::before{content:"";position:absolute;left:1px;top:6px;border-left:7px solid var(--blue);border-top:4px solid transparent;border-bottom:4px solid transparent}
.footer{height:313px;background:var(--charcoal);position:relative;color:var(--footer-text)}
.footer h2{position:absolute;top:43px;width:100%;text-align:center;font-size:20px;font-weight:700;color:var(--white)}
.footer .rule{position:absolute;top:76px;left:392px;width:26px;height:2px;background:var(--white)}
.footer-col{position:absolute;top:109px}
.footer-col h3{font-size:11.5px;font-weight:600;color:var(--white);margin-bottom:18px}
.footer-col li{list-style:none;font-size:11.2px;color:var(--footer-muted);line-height:24px;margin-left:-1px}
.bottom-bar{height:113px;background:var(--charcoal-dark);text-align:center;padding-top:25px}
.bottom-bar p{font-size:11.2px;color:#9a9a9a}
.social{display:flex;justify-content:center;gap:8px;margin-top:15px}
.social span{width:30px;height:30px;background:#4a4a4a;display:block}
</style>
</head>
<body>
<div class="site">
  <div class="lang-bar"><span>EN</span><span class="sep">|</span><span>FR</span></div>
  <header class="header">
    <div class="brand"><span class="brand-mark"></span>BRIMVAULT</div>
    <div class="phone">
      <span class="phone-icon">
        <svg width="12" height="18" viewBox="0 0 12 18"><rect x="1" y="1" width="10" height="16" rx="2" fill="none" stroke="#fff" stroke-width="1.6"/><line x1="3" y1="13" x2="9" y2="13" stroke="#fff" stroke-width="1.2"/><circle cx="6" cy="15" r=".9" fill="#fff"/></svg>
      </span>
      +33(0)155 210 480
    </div>
  </header>
  <ul class="nav">
    <li class="active" style="width:106px">ACCUIE</li>
    <li style="width:114px">PRODUITS</li>
    <li style="width:167px">VALEURS AJOUTEES</li>
    <li style="width:105px">CLIENTS</li>
    <li style="width:106px">SERVICE</li>
    <li style="width:106px">SOCIETE</li>
    <li style="width:112px">CONTACT</li>
  </ul>
  <div class="hero" role="img" aria-label="Photo d'une conseillère souriante avec casque et d'une équipe commerciale en réunion"></div>
  <main class="content">
    <section class="awards-card">
      <h2>Citations et<br>Recompenses</h2>
      <div class="rule"></div>
      <svg class="badges" width="200" height="150" viewBox="0 0 200 150" role="img" aria-label="Badges de prix et distinctions">
        <rect x="1" y="0" width="68" height="47" fill="var(--badge-navy)"/>
        <rect x="82" y="0" width="45" height="63" fill="#ffffff" stroke="#222" stroke-width="1.5"/>
        <rect x="141" y="0" width="53" height="63" fill="var(--badge-lilac)" stroke="#b9aed0" stroke-width="1"/>
        <rect x="1" y="58" width="68" height="29" fill="var(--badge-ink)"/>
        <rect x="1" y="96" width="68" height="44" fill="var(--badge-deep)"/>
        <rect x="112" y="96" width="62" height="44" fill="var(--badge-sand)"/>
      </svg>
    </section>
    <section class="partner-card">
      <span class="square"></span><span class="name">LEDGERLINE</span>
    </section>
    <article class="article">
      <h1>Le logiciel CRM Cloud</h1>
      <p>Brimvault a le plaisir de vous présenter Ledgerline CRM+. Avec plus de 16 000 clients, de la TPE‑PME à l’ETI, et plus de 2 millions d’utilisateurs, cette solution a fait ses preuves, y compris en France. Le module Ledgerline Entreprise comprend :</p>
      <ul>
        <li>Gestion du marketing : tableau de bord, saisie des plans d’action marketing, projets et tâches relevant de ces plans, suivi opérationnel et budgétaire, mesure des retours sur investissement, campagnes de marketing, notamment d’emailing, activités, analyse des réceptions, ouvertures d'email et de cliques affichant le contact qui aura cliqué et le lien qui aura été cliqué.</li>
        <li>Gestion des ventes et des forces commerciales: tableau de bord, pistes commerciales, prospects, clients, contacts, opportunités, devis, visualisation des articles, des prix et des disponibilités, suivi des commandes, visualisation des cas du support technique, prévisions commerciales, outils collaboratifs, possibilité de création et de partage de base de données « sales kit », gestion des notes de frais, visualisation des commissions, activités.</li>
      </ul>
    </article>
  </main>
  <footer class="footer">
    <h2>QUICK LINK</h2>
    <div class="rule"></div>
    <div class="footer-col" style="left:47px"><h3>PRODUITS</h3><ul><li>Crm Cloud</li><li>CRM et ERP Cloud</li><li>Multi National Cloud</li><li>Business Intelligence</li></ul></div>
    <div class="footer-col" style="left:249px"><h3>SERVICE</h3><ul><li>Strategie</li><li>Optimisation web</li><li>Consulting</li><li>Developpement</li><li>Formation</li></ul></div>
    <div class="footer-col" style="left:428px"><h3>MORE LINKS</h3><ul><li>Nos Services</li><li>Conseil</li><li>Support</li><li>Developpemetn</li><li>Formation</li><li>Devouvertie</li></ul></div>
    <div class="footer-col" style="left:626px"><h3>QUICK CONTACT</h3><ul><li>Tel:&nbsp; +33(0) 155 210 480</li><li>SAV: support@brimvault.com</li><li>Tel: +33(0) 244 610 382</li></ul></div>
  </footer>
  <div class="bottom-bar">
    <p>Copyright © 2014 Brimvault . Allright Reserved</p>
    <div class="social">
      <span aria-label="Réseau social 1"></span><span aria-label="Réseau social 2"></span><span aria-label="Réseau social 3"></span><span aria-label="Réseau social 4"></span>
    </div>
  </div>
</div>
</body>
</html>
```